I need a brochure for my new company "Nine Moons". You can read all about the company at http://www.ninemoons-example.com.sg
On the website you will also get an idea of the concept of the product, as well as design. This design actually comes from a Wordpress theme.
The brochure needs to be like a print version of the website but much more summarised, high-level. I'd like to distribute it to expecting mothers at various locations such as pre-natal yoga classes. The intention is to create enough interest so these moms-to-be will surf to my website and check out what it's all about.
Target Market(s)
Expecting moms and dads (pregnant)
Industry/Entity Type
It Company
Look and feel
Each slider illustrates characteristics of the customer's brand and the style your logo design should communicate.

```html
<!DOCTYPE html>
<html lang="en">
<head>
<meta charset="utf-8">
<title>Nine Moons – Brochure Spread</title>
<link href="https://fonts.googleapis.com/css2?family=Oswald:wght@300;500;600&family=Open+Sans:wght@400;700&family=Gochi+Hand&display=swap" rel="stylesheet">
<style>
  :root{
    --backdrop:#1d1d1d;
    --paper:#f3f0e9;
    --paper-light:#fbfaf6;
    --rule:#bdb7ab;
    --ink:#3b3937;
    --ink-soft:#55514c;
    --accent:#9c5a2b;
    --photo-a:#6c5a48;
    --photo-b:#c9a892;
    --toy-a:#c9e2c4;
    --toy-b:#e9c9dc;
    --toy-c:#bcd5ea;
  }
  *{box-sizing:border-box;margin:0;padding:0}
  html,body{width:1200px;height:799px;overflow:hidden;background:var(--backdrop)}
  body{font-family:"Open Sans",Arial,sans-serif;color:var(--ink)}

  .spread{position:absolute;left:40px;top:60px;width:1120px;height:680px;display:flex;box-shadow:0 14px 40px rgba(0,0,0,.55)}
  .page{position:relative;width:560px;height:680px;background:var(--paper);overflow:hidden}
  .page--left{border-right:1px solid #ddd6c8}
  .page--right{box-shadow:inset 18px 0 22px -18px rgba(0,0,0,.18)}

  .band{position:absolute;left:0;bottom:0;width:560px;height:220px}
  .band__text{position:absolute;left:0;right:0;text-align:center;font-size:19px;line-height:1.5;color:var(--ink)}

  .intro-heading{position:absolute;left:30px;right:30px;top:48px;text-align:center;font-family:"Oswald",Impact,sans-serif;font-weight:600;font-size:19px;line-height:1.35;letter-spacing:.3px;color:var(--accent);text-transform:uppercase}

  .story{position:absolute;left:0;right:0;top:128px;height:420px;background:var(--paper-light)}
  .story__block{position:absolute;left:36px;right:36px;font-size:14px;line-height:1.7;color:var(--ink-soft)}
  .story__block b{color:var(--ink)}
  .rule{position:absolute;left:0;right:0;border-top:1.5px dashed var(--rule)}

  .founder-photo{position:absolute;left:40px;top:152px;width:150px;height:112px;background:linear-gradient(135deg,var(--photo-a),var(--photo-b));border:7px solid #fff;box-shadow:0 2px 6px rgba(0,0,0,.35)}
  .founder-text{left:210px;top:150px;right:36px}

  .services-title{position:absolute;left:0;right:0;top:24px;text-align:center;font-family:"Oswald",Impact,sans-serif;font-weight:300;font-size:28px;color:var(--ink)}
  .services-title .brand-name{font-family:"Gochi Hand",cursive;font-weight:400;font-size:30px}
  .services{position:absolute;left:0;right:0;top:82px;height:380px;display:flex}
  .services__col{position:relative;text-align:center;padding-top:18px}
  .services__col--during{width:300px;border-right:1.5px dashed var(--rule)}
  .services__col--after{width:260px}
  .services__heading{font-family:"Oswald",Impact,sans-serif;font-weight:600;font-size:18px;text-transform:uppercase;color:var(--ink);margin-bottom:8px}
  .services__list{list-style:none;font-size:13px;line-height:24px;color:var(--ink-soft)}

  .toy-art{position:absolute;left:95px;top:210px;width:140px;height:140px;border-radius:10px;background:linear-gradient(160deg,var(--toy-c),var(--toy-a) 55%,var(--toy-b))}
</style>
</head>
<body>
  <div class="spread">
    <section class="page page--left">
      <h2 class="intro-heading">Relax.... and let us take care of planning, organising<br>and preparing for the arrival of your little one!</h2>

      <div class="story">
        <div class="rule" style="top:0"></div>
        <p class="story__block" style="top:22px"><b>Nine Moons</b> is a <b>Baby Planning &amp; Maternity Concierge</b> that lets busy moms and dads relax while we take care of all the planning. First-time parents are relieved for the guidance, and experienced parents just appreciate the extra set of hands and brains!</p>
        <div class="rule" style="top:134px"></div>
        <div class="founder-photo" role="img" aria-label="Photo of the founder holding her baby"></div>
        <p class="story__block founder-text"><b>Nine Moons</b> was founded by <b>Clara Mendoza</b> keeping in busy working moms out there, who want this to be a wonderful journey with no stress.</p>
        <div class="rule" style="top:286px"></div>
        <p class="story__block" style="top:302px;text-align:center">Her passion for the world of babies made this the perfect dreamjob for her!</p>
      </div>

      <svg class="band" viewBox="0 0 560 220" aria-hidden="true">
        <defs>
          <linearGradient id="bandLeft" x1="0" y1="0" x2="0" y2="1">
            <stop offset="0" stop-color="#f4e3c0"/><stop offset="1" stop-color="#e9cf9c"/>
          </linearGradient>
        </defs>
        <path d="M0 30 Q40 70 140 70 L470 70 Q540 70 560 20 L560 220 L0 220 Z" fill="url(#bandLeft)"/>
        <path d="M0 30 Q40 70 140 70 L470 70 Q540 70 560 20" fill="none" stroke="#fff" stroke-width="4"/>
      </svg>
      <p class="band__text" style="bottom:58px">That's how <b>Nine Moons</b> was born – to help busy moms and<br>dads with the hard stuff so you can sit back and relax.</p>
    </section>

    <section class="page page--right">
      <h2 class="services-title">How <span class="brand-name">Nine Moons</span> can help you!</h2>
      <div class="rule" style="top:78px"></div>
      <div class="services">
        <div class="services__col services__col--during">
          <h3 class="services__heading">During pregnancy...</h3>
          <ul class="services__list">
            <li>The Pregnancy Action Plan</li>
            <li>Product reviews and suggestions</li>
            <li>Nursery Setup &amp; Design</li>
            <li>Layette Shopping</li>
            <li>Baby Shower Planning</li>
            <li>Sourcing for Confinement Nanny</li>
            <li>Newborn Care</li>
            <li>Baby Registry Setup</li>
            <li>Birth Planning</li>
            <li>Baby Announcement</li>
            <li>Health, Happiness &amp; Well-Being</li>
            <li>Advice &amp; Consultation</li>
            <li>Concierge Service</li>
          </ul>
        </div>
        <div class="services__col services__col--after">
          <h3 class="services__heading">After birth...</h3>
          <ul class="services__list">
            <li>Newborn Care (up to 12 mths)</li>
            <li>Postpartum Support</li>
            <li>Asian Confinement Traditions</li>
            <li>Nanny / Childcare Sourcing</li>
            <li>Baby Food Making</li>
          </ul>
          <div class="toy-art" role="img" aria-label="Illustration of stacked pastel baby alphabet blocks with a rattle and pacifier"></div>
        </div>
      </div>

      <svg class="band" viewBox="0 0 560 220" aria-hidden="true">
        <defs>
          <linearGradient id="bandRight" x1="0" y1="0" x2="0" y2="1">
            <stop offset="0" stop-color="#f4e3c0"/><stop offset="1" stop-color="#e9cf9c"/>
          </linearGradient>
        </defs>
        <path d="M0 20 Q20 70 90 70 L420 70 Q520 70 560 30 L560 220 L0 220 Z" fill="url(#bandRight)"/>
        <path d="M0 20 Q20 70 90 70 L420 70 Q520 70 560 30" fill="none" stroke="#fff" stroke-width="4"/>
      </svg>
      <p class="band__text" style="bottom:90px;font-size:22px">So much to do and think about!</p>
    </section>
  </div>
</body>
</html>
```